Flyer-Design für Kreativwerkstatt
Zielgruppe
Kreativwerkstatt für Touristen - vorrangig Frauen
Aufgabenstellung
1 mal gefaltet
Wenn möglich außer dem Logo noch folgenden Text verwenden
Kreativität fängt da ,wo der Verstand aufhört das denken zu behindern

```html
<!DOCTYPE html>
<html lang="de">
<head>
<meta charset="utf-8">
<title>Faltenhof Kreativwerkstatt – Flyer</title>
<link href="https://fonts.googleapis.com/css2?family=Questrial&display=swap" rel="stylesheet">
<style>
  :root{
    --bg:#d9d4d2;
    --paper-1:#fef4c9;
    --paper-2:#fde8a6;
    --orange:#e2661a;
    --orange-soft:#e98a2c;
    --fold:rgba(190,150,80,.25);
    --engraving:#b9ad92;
    --handpaper:#d9cfb6;
    --photo-warm:#a98866;
    --photo-dark:#3a2e2a;
    --photo-light:#e8e4e2;
    --workshop:#8c8377;
  }
  *{margin:0;padding:0;box-sizing:border-box}
  html,body{width:1200px;height:652px;overflow:hidden;background:var(--bg)}
  body{position:relative;font-family:"Questrial",sans-serif;color:var(--orange)}
  .spread{position:absolute;left:100px;width:995px;height:263px;overflow:hidden;
    background:linear-gradient(100deg,var(--paper-1) 0%,var(--paper-2) 48%,var(--paper-1) 50%,var(--paper-2) 100%);}
  .spread--outside{top:40px}
  .spread--inside{top:350px}
  .fold{position:absolute;top:0;bottom:0;width:1px;background:var(--fold)}
  .abs{position:absolute;white-space:nowrap;line-height:1.1}
  .kicker{font-size:10px}
  .headline{font-size:18px}
  .title{font-size:24px;letter-spacing:.3px}
  .course h3{font-size:7.5px;font-weight:400;letter-spacing:.3px}
  .course p{font-size:7.5px;line-height:8.7px;white-space:normal;width:120px;color:var(--orange-soft)}
  .price{font-size:9.5px}
  .contact{font-size:5.6px;line-height:6.6px;color:var(--orange-soft)}
  .cta{font-size:13px}
  .cta-sub{font-size:7px}
  .quote{font-size:9.5px;line-height:10.6px}
  .brand{font-size:24px;color:var(--orange)}
  .brand-ring{position:absolute;border:1.5px solid var(--orange);border-radius:50%}
  .offer h3{font-size:8.5px;font-weight:400;letter-spacing:.4px}
  .offer p{font-size:7.5px;line-height:8.8px;white-space:normal;width:125px;color:var(--orange-soft)}
  .offer-photo{position:absolute;width:125px;height:67px}
  .about h3{font-size:8px;font-weight:400;letter-spacing:.4px}
  .about p{font-size:7.5px;line-height:8.8px;white-space:normal;width:198px;text-align:justify;color:var(--orange-soft)}
  .claim{font-size:12.5px;letter-spacing:.6px}
</style>
</head>
<body>

<!-- Außenseite -->
<section class="spread spread--outside">
  <div class="fold" style="left:490px"></div>

  <p class="abs kicker" style="left:25px;top:27px">Altes Handwerk neu belebt</p>
  <p class="abs headline" style="left:38px;top:42px">eine besondere Auszeit -</p>
  <p class="abs headline" style="left:76px;top:63px">Papierhandwerk erlernen</p>

  <div class="abs" role="img" aria-label="Historischer Stich: Papiermacher schöpft Papier an einem Holzbottich"
       style="left:318px;top:12px;width:127px;height:83px;background:linear-gradient(180deg,transparent 0%,var(--engraving) 70%,transparent 100%);opacity:.7;border-radius:40% 40% 20% 20%"></div>

  <div class="abs course" style="left:35px;top:117px">
    <h3>SCHNUPPERKURS</h3>
    <p>Interessierte, die sich gerne mit dem Werkstoff Papier beschäf-tigen, erlernen unter fachkun-diger Anleitung die Grundlagen des Buchbinderhandwerks ......</p>
  </div>
  <div class="abs course" style="left:189px;top:117px">
    <h3>EINSTIEGERKURS</h3>
    <p>Interessierte, die sich gerne mit dem Werkstoff Papier beschäf-tigen, erlernen unter fachkun-diger Anleitung die Grundlagen des Buchbinderhandwerks ......</p>
  </div>
  <div class="abs course" style="left:343px;top:117px">
    <h3>FORTGESCHRITTENENKURS</h3>
    <p>Interessierte, die sich gerne mit dem Werkstoff Papier beschäf-tigen, erlernen unter fachkun-diger Anleitung die Grundlagen des Buchbinderhandwerks ......</p>
  </div>
  <p class="abs price" style="left:138px;top:176px">€ 80,-</p>
  <p class="abs price" style="left:291px;top:176px">€ 120,-</p>
  <p class="abs price" style="left:438px;top:177px">€ 220,-</p>

  <svg class="abs" style="left:34px;top:214px" width="8" height="11" viewBox="0 0 8 11" aria-hidden="true">
    <path d="M4 0.5a3.3 3.3 0 0 0-3.3 3.3C0.7 6.3 4 10.5 4 10.5s3.3-4.2 3.3-6.7A3.3 3.3 0 0 0 4 0.5z" fill="var(--orange-soft)"/>
    <circle cx="4" cy="3.8" r="1.3" fill="var(--paper-1)"/>
  </svg>
  <p class="abs contact" style="left:48px;top:213px">Kreativwerkstatt<br>Faltenhof<br>Lindenweg 12<br>12345 MUSTERSTADT</p>
  <svg class="abs" style="left:110px;top:213px" width="9" height="20" viewBox="0 0 9 20" aria-hidden="true">
    <text x="0" y="7" font-size="8" fill="var(--orange-soft)" font-family="sans-serif">@</text>
    <path d="M2 11c-1 1 0 4 2.5 6l1.2-1.2-1.5-1.5-.8.6C2.7 14 2.2 13 2.3 12.3l.8-.5-1-1.5z" fill="var(--orange-soft)"/>
  </svg>
  <p class="abs contact" style="left:122px;top:213px">faltenhof.de<br>kreativwerkstatt@faltenhof<br>0176 000 12345</p>

  <p class="abs cta" style="left:238px;top:212px">jetzt anmelden</p>
  <p class="abs cta-sub" style="left:247px;top:231px">und eine besondere Auszeit erleben</p>

  <!-- rechte Seite -->
  <svg class="abs" style="left:490px;top:50px" width="280" height="213" viewBox="0 0 280 213" role="img" aria-label="Handgeschöpftes Papier mit eingearbeiteten Blüten und Blättern">
    <path d="M0 95 L30 70 L55 78 L80 40 L120 45 L140 12 L165 20 L190 8 L210 40 L235 60 L245 100 L275 130 L268 170 L250 200 L240 213 L0 213 Z" fill="var(--handpaper)"/>
  </svg>
  <p class="abs title" style="left:510px;top:25px">PAPIERHANDWERK</p>
  <p class="abs title" style="left:510px;top:53px">erlernen</p>

  <div class="brand-ring" style="left:840px;top:2px;width:160px;height:132px"></div>
  <p class="abs brand" style="left:868px;top:55px">Faltenhof</p>

  <p class="abs quote" style="left:787px;top:218px">Kreativität fängt da an,</p>
  <p class="abs quote" style="left:801px;top:229px">wo der Verstand aufhört</p>
  <p class="abs quote" style="left:818px;top:240px">das Denken zu behindern</p>
</section>

<!-- Innenseite -->
<section class="spread spread--inside">
  <div class="fold" style="left:497px"></div>

  <p class="abs title" style="left:35px;top:20px">WERKSTOFF PAPIER</p>
  <p class="abs headline" style="left:150px;top:48px;font-size:13.5px">Altes Handwerk - moderne Materialien</p>

  <div class="abs offer" style="left:34px;top:88px">
    <h3>PAPIERSCHÖPFEN</h3>
  </div>
  <div class="offer-photo" role="img" aria-label="Hände beim Papierschöpfen über einem Holzbottich" style="left:35px;top:101px;background:linear-gradient(135deg,#c7b48f,var(--photo-warm))"></div>
  <div class="abs offer" style="left:34px;top:181px"><p>Lerne Dein eigenes besonderes Papier herzustellen</p></div>

  <div class="abs offer" style="left:195px;top:88px"><h3>BUCHBINDEN</h3></div>
  <div class="offer-photo" role="img" aria-label="Hände beim Binden eines Buches mit Faden" style="left:195px;top:101px;background:linear-gradient(135deg,#5a3a26,#a57850)"></div>
  <div class="abs offer" style="left:194px;top:181px"><p>Gestalte Dein eigenes Buch und setze es durch Leder richtig in Szene.</p></div>

  <div class="abs offer" style="left:353px;top:88px"><h3>KASSETTEN</h3></div>
  <div class="offer-photo" role="img" aria-label="Schwarze Geschenkkassette mit rotem Innenrand" style="left:353px;top:102px;background:linear-gradient(135deg,var(--photo-light),#bfb8b5)"></div>
  <div class="abs offer" style="left:353px;top:181px"><p>Kreiere einen „Schuhkarton“ als Schatzkiste</p></div>

  <div class="abs" role="img" aria-label="Werkstatt mit Arbeitstischen, Pressen und Regalen" style="left:522px;top:60px;width:193px;height:137px;background:linear-gradient(160deg,#d8d4cc,var(--workshop) 60%,#5e554c)"></div>
  <div class="abs" role="img" aria-label="Porträt der Werkstattinhaberin bei der Arbeit" style="left:689px;top:33px;width:52px;height:87px;background:linear-gradient(180deg,#c9b5a4,var(--photo-dark))"></div>

  <div class="brand-ring" style="left:840px;top:-2px;width:160px;height:132px"></div>
  <p class="abs brand" style="left:868px;top:51px">Faltenhof</p>

  <div class="abs about" style="left:727px;top:125px">
    <h3>ÜBER MICH</h3>
  </div>
  <div class="abs about" style="left:727px;top:143px">
    <p>Lorem ipsum dolor sit amet, consetetur sadipscing elitr, sed diam nonumy eirmod tempor invidunt ut labore et dolore magna aliquyam erat, sed diam voluptua. At vero eos et accusam et justo duo dolores et ea rebum. Stet clita kasd gubergren, no sea takimata sanctus est Lorem ipsum dolor sit amet. Lorem ipsum dolor sit amet, consetetur sadipscing elitr, sed diam</p>
  </div>

  <p class="abs claim" style="left:135px;top:235px">Wir möchten Dich mit traditionellem Handwerk rund um das Papier vertraut machen!</p>
</section>

</body>
</html>
```